Gadri Management - Managing Urban Projects for the City of Modiin

Gadri Management needs a website that projects its professionalism and innovation to the residents of the city of Modiin. The design needs include: 1) a homepage design, 2) ~12 customized icons used on the homepage, 3) a layered image (city landscape with company logo on it) used as a fullwidth background image on the homepage. The client wants a site that is pleasant on the eye and easy to navigate. The client wants the site to project the organization as being professional and innovative.

Target Market(s)

adult residents of the city of modiin, israel

Industry/Entity Type

management of urban projects

Number of Pages Required

1 page

Font styles to use
Sans Serif

Requirements
Must have
• psd of design and psd of main fullwidth background image on the homepage
Nice to have
• icons for navigation bar and homepage teasers
Should not have
• colors should match the logo attached, font should be modern

```html
<!DOCTYPE html>
<html lang="en">
<head>
<meta charset="utf-8">
<title>Gadri Management</title>
<link rel="stylesheet" href="https://fonts.googleapis.com/css2?family=Roboto:wght@300;400;500;700&display=swap">
<style>
:root{
  --green:#2e8b2e;
  --green-bright:#3fae1b;
  --card-green:rgba(52,158,40,.92);
  --nav-dark:#0c1a07;
  --text-grey:#6b6b6b;
  --input-bg:#e9f3e9;
  --input-border:#cfdccf;
  --footer:#1e1e1e;
  --white:#fff;
}
*{margin:0;padding:0;box-sizing:border-box}
html,body{width:1200px;height:2507px;overflow:hidden}
body{font-family:'Roboto',sans-serif;background:var(--white);position:relative;color:#222}

/* hero */
.hero{position:absolute;left:0;top:0;width:1200px;height:580px;overflow:hidden}
.hero-photo{position:absolute;inset:0;background:linear-gradient(180deg,#5b8cc8 0%,#9ab8d8 28%,#b9c4cc 42%,#9a9a90 55%,#8a8a7c 70%,#6f7a62 85%,#5d6a52 100%)}
.brand{position:absolute;left:0;width:1049px;top:120px;text-align:center}
.brand-mark{display:inline-block;width:34px;height:34px;border-radius:50%;background:var(--green);vertical-align:middle;margin-right:12px}
.brand-name{display:inline-block;vertical-align:middle;font-size:34px;font-weight:700;color:var(--green)}
.teasers{position:absolute;left:228px;top:371px;display:flex;gap:6px}
.teaser{width:170px;height:164px;background:var(--card-green);border-radius:34px 44px 0 0;text-align:center;color:var(--white);padding-top:32px}
.teaser svg{display:block;margin:0 auto 12px}
.teaser h3{font-size:14px;font-weight:500;margin-bottom:10px}
.teaser a{font-size:8px;color:var(--white);text-decoration:underline}
.scroll-tab{position:absolute;left:576px;top:564px;width:48px;height:30px;background:var(--white);border-radius:24px 24px 0 0;text-align:center}
.scroll-tab svg{margin-top:8px}

.sidenav{position:absolute;left:1049px;top:0;width:151px;height:580px;background:var(--nav-dark)}
.sidenav a{display:flex;align-items:center;height:64.5px;border-bottom:1px solid #24331c;color:#e8e8e8;font-size:11px;line-height:15px;text-decoration:none;padding-left:10px;gap:8px}
.sidenav a.active{background:var(--green-bright);margin-left:3px;padding-left:7px}
.sidenav svg{flex:0 0 26px}

/* about */
.section-mark{display:block;margin:0 auto;width:22px;height:22px;border-radius:50%;background:var(--green)}
.about{position:absolute;top:674px;left:0;width:1200px;text-align:center}
.about .eyebrow{font-size:18px;color:#222;margin-top:12px}
.section-title{font-size:37px;font-weight:700;color:var(--green);line-height:44px}
.about p{font-size:13.5px;font-weight:300;color:var(--text-grey);line-height:22.5px;width:740px;margin:0 auto}
.about .lead{margin-top:14px}
.about .gap{margin-top:22px}
.btn{display:inline-block;background:var(--green);color:var(--white);font-size:13px;font-weight:500;border-radius:3px;box-shadow:3px 3px 0 #c9e6c0}
.about .btn{margin-top:36px;width:166px;height:44px;line-height:44px}

/* projects */
.projects{position:absolute;top:1150px;left:0;width:1200px;height:565px;background:linear-gradient(180deg,#ffffff 0%,#e7efe3 18%,#c8e0b3 40%,#a3cf7c 70%,#8ac350 100%)}
.projects .section-mark{margin-top:50px}
.projects .section-title{text-align:center;margin-top:8px}
.arrows{position:absolute;left:1010px;top:112px;display:flex;gap:14px}
.project{position:absolute;top:162px;width:315px}
.project-photo{width:315px;height:288px}
.project-caption{position:absolute;left:10px;top:269px;width:255px;height:57px;background:var(--white);font-size:18.5px;padding:0 15px;line-height:57px;color:#111}
.project-caption.featured{background:var(--green);color:#cfeec4}

/* contact */
.contact{position:absolute;top:1789px;left:0;width:1200px;text-align:center}
.contact .section-title{margin-top:10px}
.field{position:absolute;height:42px;background:var(--input-bg);border:1px solid var(--input-border);border-radius:2px;font-size:15px;color:#666;line-height:40px;padding-left:15px}
.submit{position:absolute;left:855px;top:1973px;width:233px;height:42px;line-height:42px;text-align:center;background:var(--green);color:var(--white);font-size:15px;font-weight:700;border-radius:2px}

/* footer */
.footer{position:absolute;top:2117px;left:0;width:1200px;height:390px;background:var(--footer);color:#bdbdbd}
.footer h4{position:absolute;top:52px;font-size:19px;font-weight:500;color:#e8e8e8}
.footer h4::after{content:"";display:block;width:48px;height:2px;background:var(--green-bright);margin-top:8px}
.footer .about-text{position:absolute;left:111px;top:104px;width:305px;font-size:11.5px;line-height:19.4px;font-weight:300}
.details{position:absolute;left:524px;top:104px;font-size:11.5px;color:#e8e8e8}
.details .val{color:var(--green-bright);font-size:15px;margin:2px 0 13px;line-height:19px}
.links{position:absolute;top:104px;font-size:11.5px;line-height:19.4px;font-weight:300;list-style:none}
.copyright{position:absolute;top:2440px;left:0;width:1200px;text-align:center;font-size:10.5px;color:#d8d8d8}
</style>
</head>
<body>

<header class="hero">
  <div class="hero-photo" role="img" aria-label="Aerial view of the city under a blue sky"></div>
  <div class="brand"><span class="brand-mark"></span><span class="brand-name">Gadri Management</span></div>

  <div class="teasers">
    <div class="teaser">
      <svg width="44" height="42" viewBox="0 0 44 42" fill="none" stroke="#fff" stroke-width="2"><rect x="3" y="2" width="26" height="36" rx="2"/><path d="M8 10l3 3 5-6M8 20h14M8 26h10M8 32h8"/><path d="M38 8l4 4-16 18-5 1 1-5z"/></svg>
      <h3>Title Here</h3><a>Learn More</a>
    </div>
    <div class="teaser">
      <svg width="44" height="42" viewBox="0 0 44 42" fill="none" stroke="#fff" stroke-width="2"><rect x="3" y="2" width="26" height="36" rx="2"/><path d="M8 10l3 3 5-6M8 20h14M8 26h10M8 32h8"/><path d="M38 8l4 4-16 18-5 1 1-5z"/></svg>
      <h3>Title Here</h3><a>Learn More</a>
    </div>
    <div class="teaser">
      <svg width="44" height="42" viewBox="0 0 44 42" fill="none" stroke="#fff" stroke-width="2"><rect x="3" y="2" width="26" height="36" rx="2"/><path d="M8 10l3 3 5-6M8 20h14M8 26h10M8 32h8"/><path d="M38 8l4 4-16 18-5 1 1-5z"/></svg>
      <h3>Title Here</h3><a>Learn More</a>
    </div>
    <div class="teaser">
      <svg width="44" height="42" viewBox="0 0 44 42" fill="none" stroke="#fff" stroke-width="2"><rect x="3" y="2" width="26" height="36" rx="2"/><path d="M8 10l3 3 5-6M8 20h14M8 26h10M8 32h8"/><path d="M38 8l4 4-16 18-5 1 1-5z"/></svg>
      <h3>Title Here</h3><a>Learn More</a>
    </div>
  </div>
  <div class="scroll-tab"><svg width="14" height="10" viewBox="0 0 14 10" fill="none" stroke="#333" stroke-width="1.5"><path d="M2 2l5 6 5-6"/></svg></div>

  <nav class="sidenav">
    <a class="active"><svg width="26" height="26" viewBox="0 0 26 26" fill="none" stroke="#fff" stroke-width="1.5"><path d="M3 12L13 3l10 9M6 10v13h14V10M11 23v-7h4v7"/></svg>Home</a>
    <a><svg width="26" height="26" viewBox="0 0 26 26" fill="none" stroke="#fff" stroke-width="1.5"><circle cx="13" cy="13" r="10"/><path d="M13 11v7M13 7v1"/></svg>About</a>
    <a><svg width="26" height="26" viewBox="0 0 26 26" fill="none" stroke="#fff" stroke-width="1.5"><path d="M3 10h4l10-6v18L7 16H3zM7 16l2 6h3M20 9l4-2M20 13h4M20 17l4 2"/></svg>Business<br>Promotion</a>
    <a><svg width="26" height="26" viewBox="0 0 26 26" fill="none" stroke="#fff" stroke-width="1.5"><rect x="2" y="4" width="15" height="19"/><path d="M5 9h9M5 13h6M5 17h5"/><circle cx="19" cy="18" r="6"/><path d="M19 15v3l2 2"/></svg>Project<br>Management</a>
    <a><svg width="26" height="26" viewBox="0 0 26 26" fill="none" stroke="#fff" stroke-width="1.5"><path d="M2 10h22v13H2zM4 6h18l2 4H2zM6 14h5v9M15 14h5v4h-5z"/></svg>Tech and<br>Commercial Areas</a>
    <a><svg width="26" height="26" viewBox="0 0 26 26" fill="none" stroke="#fff" stroke-width="1.5"><rect x="6" y="2" width="14" height="16"/><path d="M9 6h8M9 10h8M9 14h5M4 22h18M8 18l-2 4M18 18l2 4"/></svg>Tenders</a>
    <a><svg width="26" height="26" viewBox="0 0 26 26" fill="none" stroke="#fff" stroke-width="1.5"><rect x="3" y="3" width="18" height="21"/><path d="M6 7h12M6 11h5v5H6zM14 11h4M14 15h4M6 19h12"/></svg>Signage<br>and Publication</a>
    <a><svg width="26" height="26" viewBox="0 0 26 26" fill="none" stroke="#fff" stroke-width="1.5"><rect x="2" y="8" width="20" height="15"/><path d="M5 8l3-5h10l3 5M6 13h6M6 17h10M17 13h2"/></svg>Projects</a>
    <a><svg width="26" height="26" viewBox="0 0 26 26" fill="none" stroke="#fff" stroke-width="1.5"><path d="M5 9c0 7 5 13 12 13l2-3-4-3-2 2c-2-1-5-4-6-6l2-2-3-4z"/><path d="M15 3a8 6 0 1 1 2 11l-3 1 1-3"/></svg>Contact</a>
  </nav>
</header>

<section class="about">
  <span class="section-mark"></span>
  <p class="eyebrow">About Us</p>
  <h2 class="section-title">Welcome to Gadri Manager</h2>
  <p class="lead">Nofim Heights.<br>The director is responsible for the management of the technology park (Telem), the Shaked center (Nofar), the Tamar park, the municipal sports center including the municipal pool, the transportation center, the municipal signage and more.</p>
  <p class="gap">As part of this activity, the management promotes and markets areas in the technology park (Telem) and the Shaked center (Nofar), in conjunction with the regional land office. The director also accompanies the entrepreneurs in various areas - from the tender stage to the stage of moving to the new residence.</p>
  <span class="btn">Learn More About Us</span>
</section>

<section class="projects" role="group" aria-label="Our Projects">
  <span class="section-mark"></span>
  <h2 class="section-title">Our Projects</h2>
  <div class="arrows">
    <svg width="34" height="14" viewBox="0 0 34 14" fill="none" stroke="#fff" stroke-width="1.5"><path d="M33 7H2M8 1L2 7l6 6"/></svg>
    <svg width="34" height="14" viewBox="0 0 34 14" fill="none" stroke="#fff" stroke-width="1.5"><path d="M1 7h31M26 1l6 6-6 6"/></svg>
  </div>
  <article class="project" style="left:111px">
    <div class="project-photo" role="img" aria-label="Park lake at dusk" style="background:linear-gradient(180deg,#2a2d36 0%,#4a3f3a 45%,#6b4f38 60%,#1f2226 100%)"></div>
    <div class="project-caption">Tamar Park</div>
  </article>
  <article class="project" style="left:441px">
    <div class="project-photo" role="img" aria-label="Bus at the transportation center platform" style="background:linear-gradient(180deg,#9c9c98 0%,#cfd0cc 40%,#8f9192 70%,#6c6c68 100%)"></div>
    <div class="project-caption featured">The Transportation Center</div>
  </article>
  <article class="project" style="left:771px">
    <div class="project-photo" role="img" aria-label="Aerial view of the technology park office buildings" style="background:linear-gradient(180deg,#7f8c99 0%,#6b7780 35%,#5e6a66 65%,#4c5448 100%)"></div>
    <div class="project-caption">The Technology Park</div>
  </article>
</section>

<section class="contact">
  <span class="section-mark"></span>
  <h2 class="section-title">Contact us</h2>
</section>
<div class="field" style="left:111px;top:1921px;width:316px">First Name</div>
<div class="field" style="left:442px;top:1921px;width:316px">Laste Name</div>
<div class="field" style="left:772px;top:1921px;width:316px">Phone</div>
<div class="field" style="left:111px;top:1973px;width:316px">Email Address</div>
<div class="field" style="left:442px;top:1973px;width:399px">Message</div>
<div class="submit">Submit Now</div>

<footer class="footer">
  <h4 style="left:111px">About Gadri</h4>
  <p class="about-text">Gadri Management is the professional body that manages, oversees and accompanies urban projects for the benefit of the public in the city of Nofim Heights. The director is responsible for the management of the technology park (Telem), the Shaked center (Nofar), the Tamar park, the municipal sports center including the municipal pool, the transportation center, the municipal signage and more.</p>
  <h4 style="left:524px">Contact Details</h4>
  <div class="details">
    <div>Phone</div><div class="val">08-9410273</div>
    <div>Fax</div><div class="val">08-9410274</div>
    <div>Address</div><div class="val">Cedar Grove 18,<br>Nofim</div>
  </div>
  <h4 style="left:783px">Sitemap</h4>
  <ul class="links" style="left:783px"><li>Home</li><li>About</li><li>Business Promotion</li><li>Project Management</li><li>Tech and Commercial Areas</li></ul>
  <ul class="links" style="left:959px"><li>Tenders</li><li>Signage and Publication</li><li>Projects</li><li>Contact</li></ul>
</footer>
<p class="copyright">Directorate of Gadri - Nofim | Heights www.gadri-mgmt.example©All rights reserved Accessibility arrangements</p>

</body>
</html>
```